Business card design for counselling and psychotherapy practice

I am seeking a business card for a new venture into private practice. I am based in Brisbane Qld Australia. I provide holistic counselling and psychotherapy to individuals and groups.
Some words that describe the underpinnings of this practice would include: being, becoming, awareness, wholeness, contact, safety, acceptance, relationship, gestalt, paradox, interconnected, nature, process.
I would like to see designs that include earth colours.
The overall design should communicate safety and a curiosity of being and becoming.
Target Market(s)
this design is marketed toward women, professionals, lesbian, transgender, mothers
Industry/Entity Type
Safety
Contact Information for Business Card
Still Harbour
Counselling and Psychotherapy
Wren Callow
ph: 0412739506
email: wren.stillharbour@examplemail.test
www.stillharbourcounselling&psychotherapy.test
Logo styles of interest
Abstract Logo
Look and feel

```html
<!DOCTYPE html>
<html lang="en">
<head>
<meta charset="utf-8">
<title>Still Harbour – Business Card</title>
<link rel="stylesheet" href="https://fonts.googleapis.com/css2?family=Tinos&family=EB+Garamond:wght@400&display=swap">
<style>
  :root {
    --peach: #e8bf9c;
    --peach-deep: #e5b894;
    --cream-corner: #eedccd;
    --seed-light: rgba(248, 232, 214, 0.85);
    --seed-fade: rgba(248, 232, 214, 0);
    --ink: #111111;
    --slate: #5d6066;
    --rule: #6a6b70;
    --contact: #6b6866;
    --name: #1c1c1c;
  }
  html, body {
    margin: 0;
    padding: 0;
    overflow: hidden;
    background: #ffffff;
  }
  .card {
    position: relative;
    width: 1200px;
    height: 693px;
    overflow: hidden;
    background:
      radial-gradient(ellipse 420px 320px at 1200px 0px, var(--cream-corner), rgba(238,220,205,0) 100%),
      radial-gradient(ellipse 360px 260px at 0px 693px, var(--cream-corner), rgba(238,220,205,0) 100%),
      linear-gradient(135deg, var(--peach) 0%, var(--peach-deep) 55%, var(--peach) 100%);
  }
  .seedhead {
    position: absolute;
    border-radius: 50%;
    background: radial-gradient(circle, var(--seed-light) 0%, rgba(248,232,214,0.45) 45%, var(--seed-fade) 75%);
  }
  .seedhead--main { left: 20px; top: 60px; width: 580px; height: 600px; }
  .seedhead--drift-a { left: 660px; top: 90px; width: 160px; height: 190px; }
  .seedhead--drift-b { left: 935px; top: 160px; width: 130px; height: 150px; }
  .seedhead--drift-c { left: 1020px; top: 360px; width: 140px; height: 150px; }

  .practice-name {
    position: absolute;
    left: 0; width: 1200px;
    top: 284px;
    margin: 0;
    text-align: center;
    font-family: "Tinos", "Times New Roman", serif;
    font-weight: 400;
    font-size: 64px;
    line-height: 1;
    color: var(--ink);
  }
  .practice-tagline {
    position: absolute;
    left: 0; width: 1200px;
    top: 366px;
    margin: 0;
    text-align: center;
    font-family: "Tinos", "Times New Roman", serif;
    font-size: 38px;
    line-height: 1;
    color: var(--slate);
  }
  .divider {
    position: absolute;
    left: 224px;
    top: 422px;
    width: 752px;
    height: 12px;
  }
  .practitioner {
    position: absolute;
    right: 213px;
    top: 446px;
    margin: 0;
    font-family: "EB Garamond", Garamond, serif;
    font-size: 44px;
    line-height: 1;
    color: var(--name);
  }
  .contact {
    position: absolute;
    left: 230px;
    top: 516px;
    margin: 0;
    padding: 0;
    list-style: none;
    font-family: "EB Garamond", Garamond, serif;
    font-size: 31px;
    line-height: 45px;
    color: var(--contact);
  }
</style>
</head>
<body>
<div class="card">
  <div class="seedhead seedhead--main" role="img" aria-label="Large pale dandelion seed head illustration"></div>
  <div class="seedhead seedhead--drift-a" role="img" aria-label="Drifting dandelion seed illustration"></div>
  <div class="seedhead seedhead--drift-b" role="img" aria-label="Drifting dandelion seed illustration"></div>
  <div class="seedhead seedhead--drift-c" role="img" aria-label="Drifting dandelion seed illustration"></div>

  <h1 class="practice-name">Still Harbour</h1>
  <p class="practice-tagline">Counselling and Psychotherapy</p>

  <svg class="divider" viewBox="0 0 752 12" aria-hidden="true">
    <line x1="5" y1="6" x2="747" y2="6" stroke="var(--rule)" stroke-width="2"/>
    <circle cx="5" cy="6" r="3.5" fill="var(--rule)"/>
    <circle cx="747" cy="6" r="3.5" fill="var(--rule)"/>
  </svg>

  <p class="practitioner">Wren Callow</p>

  <ul class="contact">
    <li class="contact__phone">ph: 0412739506</li>
    <li class="contact__email">email: wren.stillharbour@examplemail.test</li>
    <li class="contact__web">www.stillharbourcounselling&amp;psychotherapy.test</li>
  </ul>
</div>
</body>
</html>
```